Chart Your Own Harbor Promotional Flyer

I Need a one page, one-sided 8.5 x 11 editable promotional flyer that POPS!, designed in photoshop

[TITLE]Chart Your Own Harbor: 3 BRIGHT Steps to Lift Your Practice Today!

[CONTENT for the Flyer:]

At this content-rich event you will learn how to:
• Get out of feast and famine mode and into six, multi-six and/or seven figure-income mode
• Leapfrog your competition and become the obvious choice in your market
• Have your business aligned with who you are and what you want
• Enjoy your business far more than you imagined possible.
• Have more fun and time to yourself
• Live free and unbound!

Accolades
“Delphine helped us increase our six figure income by 41%...I feel reborn!” Marlene & Otis Pruitt, Vienna, VA

“…Delphine is a joy to listen to - compelling, smart, provocative…” – Dwight Fennimore, Charlotte, North Carolina

“Delphine helped me increase my business by 66%...without me spending more time, money, or making cold calls! …I am in the zone!” Tess Calloway, Baltimore, MD
“Delphine is an energetic and dynamic speaker…content-rich…holds your attention to the very end!” Hal Brisbee, Frmr Pres., Kemper & Vail, MD, MD, D.C., PA, DE, NJ
“Delphine is the real estate whisperer!” Lou Tremaine, Washington D.C.

“Delphine was prepared, funny, informative and made a connection with each of our agents…Fabulous!…even my admins were PUMPED!!! – Paul Devereux, New York

About Delphine:
Delphine is a highly regarded business development speaker & coach who knows how to pump up an audience and have them making more money, in less time, AND having more fun doing it! What’s not to love?! Consistently rated as an exceptional speaker and conference favorite! Among her work: Magnet Method: How to Draw Your Dream Buyers Time After Time!, Client Pipelines Without Fuss, The Costliest Outreach Blunders Real Estate Agents Commit and How to Sidestep Them, Hard Seasons Forge Hard Sellers, Fuel for the Spirit for Real Estate Agents.

[Also need a section for:]
Date: December 9, 2015, Time: 9:00 Am - 12:00 Noon, Place: Silver Maple Conference, Ashford Hollow, PA

Target Market(s)

Real Estate Agents

Industry/Entity Type

Real Estate Agent

Font styles to use
Sans Serif

Colors
0655a3
f37122

Requirements
Must have
• the top tier prop mentor logo
Nice to have
• chart your own harbor logo; lots of POP! :-) ; open to other colors, accent colors.

```html
<!DOCTYPE html>
<html lang="en">
<head>
<meta charset="utf-8">
<title>Chart Your Own Harbor – Event Flyer</title>
<link href="https://fonts.googleapis.com/css2?family=Open+Sans:ital,wght@0,400;0,600;0,700;0,800;1,400&display=swap" rel="stylesheet">
<style>
  :root {
    --blue: #0655a3;
    --blue-dark: #053f7a;
    --orange: #f37122;
    --ink: #2b2b2b;
    --muted: #555;
    --paper: #ffffff;
    --bg: #e9eaec;
  }
  * { box-sizing: border-box; margin: 0; padding: 0; }
  html, body { width: 900px; height: 1200px; overflow: hidden; }
  body { background: var(--bg); font-family: "Open Sans", Arial, sans-serif; color: var(--ink); }
  .flyer { position: relative; width: 900px; height: 1200px; background: var(--paper); overflow: hidden; }

  .hero-photo {
    position: absolute; right: 0; top: 0; width: 470px; height: 300px;
    background: linear-gradient(160deg, #8fc6e8 0%, #bfe0a8 45%, #7fb34a 100%);
  }
  .brand { position: absolute; left: 40px; top: 50px; width: 380px; }
  .brand-name { font-size: 46px; font-weight: 800; color: var(--blue); line-height: 1.05; letter-spacing: -1px; }
  .brand-tag { margin-top: 8px; font-size: 24px; font-weight: 700; color: var(--orange); }
  .brand-dot { display: inline-block; width: 16px; height: 16px; border-radius: 50%; background: var(--orange); margin-right: 10px; vertical-align: middle; }

  .bar {
    position: absolute; left: 0; width: 900px; height: 42px; padding: 0 40px;
    background: linear-gradient(90deg, var(--blue-dark), var(--blue));
    color: #fff; font-weight: 700; font-size: 20px; line-height: 42px;
  }
  .bar .accent { color: var(--orange); }
  .bar-learn { top: 300px; }
  .bar-accolades { top: 518px; width: 430px; }
  .bar-about { top: 902px; }

  .learn-list { position: absolute; left: 40px; top: 356px; width: 820px; list-style: none; font-size: 16px; line-height: 25px; }
  .learn-list li::before { content: "•"; color: var(--orange); font-weight: 800; margin-right: 10px; }

  .quotes { position: absolute; font-size: 13px; line-height: 18px; }
  .quotes-left { left: 40px; width: 380px; top: 572px; }
  .quotes-right { left: 470px; width: 390px; top: 642px; }
  .quote { margin-bottom: 12px; }
  .quote cite { display: block; text-align: right; font-style: italic; color: var(--muted); font-size: 12px; }

  .event-box {
    position: absolute; left: 470px; top: 518px; width: 390px; height: 110px;
    background: var(--orange); color: #fff; padding: 14px 20px;
    font-size: 17px; font-weight: 700; line-height: 23px;
  }

  .about { position: absolute; left: 40px; top: 956px; width: 820px; font-size: 14px; line-height: 21px; }

  .footer-site { position: absolute; left: 40px; top: 1118px; font-size: 18px; font-weight: 700; color: var(--blue); }
  .coach-photo {
    position: absolute; left: 560px; top: 1070px; width: 130px; height: 90px;
    background: linear-gradient(180deg, #c9b49a, #6b5a4a);
  }
  .coach-name { position: absolute; left: 700px; top: 1070px; font-size: 17px; font-weight: 700; color: var(--orange); }
  .mentor-mark { position: absolute; left: 700px; top: 1096px; width: 180px; font-size: 20px; font-weight: 800; color: var(--blue); line-height: 1.05; text-transform: uppercase; }
  .footer-band { position: absolute; left: 0; bottom: 0; width: 900px; height: 40px; background: var(--blue); }
</style>
</head>
<body>
<main class="flyer">
  <div class="hero-photo" role="img" aria-label="Woman with arms raised in a sunny green field under a blue sky"></div>

  <header class="brand">
    <div class="brand-name"><span class="brand-dot"></span>Chart Your Own Harbor</div>
    <div class="brand-tag">3 BRIGHT Steps to Lift Your Practice Today!</div>
  </header>

  <div class="bar bar-learn">At this <span class="accent">content-rich</span> event you will learn how to:</div>
  <ul class="learn-list">
    <li>Get out of feast and famine mode and into six, multi-six and/or seven figure-income mode</li>
    <li>Leapfrog your competition and become the obvious choice in your market</li>
    <li>Have your business aligned with who you are and what you want</li>
    <li>Enjoy your business far more than you imagined possible.</li>
    <li>Have more fun and time to yourself</li>
    <li>Live free and unbound!</li>
  </ul>

  <div class="bar bar-accolades">Accolades:</div>
  <section class="quotes quotes-left">
    <p class="quote">“Delphine helped us increase our six figure income by 41%...I feel reborn!”<cite>Marlene &amp; Otis Pruitt, Vienna, VA</cite></p>
    <p class="quote">“…Delphine is a joy to listen to - compelling, smart, provocative…”<cite>Dwight Fennimore, Charlotte, North Carolina</cite></p>
    <p class="quote">“Delphine helped me increase my business by 66%...without me spending more time, money, or making cold calls! …I am in the zone!”<cite>Tess Calloway, Baltimore, MD</cite></p>
  </section>

  <div class="event-box">December 9, 2015, Time: 9:00 Am - 12:00 Noon, Place: Silver Maple Conference, Ashford Hollow, PA</div>
  <section class="quotes quotes-right">
    <p class="quote">“Delphine was prepared, funny, informative and made a connection with each of our agents…Fabulous!…even my admins were PUMPED!!!<cite>Paul Devereux, New York</cite></p>
    <p class="quote">“Delphine is the real estate whisperer!”<cite>Lou Tremaine, Washington D.C.</cite></p>
    <p class="quote">“Delphine is an energetic and dynamic speaker…content-rich…holds your attention to the very end!”<cite>Hal Brisbee, Frmr Pres., Kemper &amp; Vail, MD, MD, D.C., PA, DE, NJ</cite></p>
  </section>

  <div class="bar bar-about">About Delphine:</div>
  <p class="about">Delphine is a highly regarded business development speaker &amp; coach who knows how to pump up an audience and have them making more money, in less time, AND having more fun doing it! What’s not to love?! Consistently rated as an exceptional speaker and conference favorite! Among her work: Magnet Method: How to Draw Your Dream Buyers Time After Time!, Client Pipelines Without Fuss, The Costliest Outreach Blunders Real Estate Agents Commit and How to Sidestep Them, Hard Seasons Forge Hard Sellers, Fuel for the Spirit for Real Estate Agents.</p>

  <div class="footer-site">www.harborcoachdemo.com</div>
  <div class="coach-photo" role="img" aria-label="Portrait photo of speaker Delphine Ashby"></div>
  <div class="coach-name">Delphine Ashby</div>
  <div class="mentor-mark">top tier prop mentor</div>
  <div class="footer-band"></div>
</main>
</body>
</html>
```